Etiketten für Weinbaubetrieb
Recht herzlichen Dank für die rasche Umsetzung und die punktgenaue Umsetzung von diversen Wünschen. Das Design hat uns schwer begeistert, wir hoffen dass dieses genauso gut ankommt bei unseren Kunden wie bei uns.
Zielgruppe
Weinbaubetrieb
Aufgabenstellung
Wollen ein neues Flaschen-Etikett für unsere Wein Magnumflaschen kreieren (Limitierte Stückzahl), Hintergrund soll Schwarz sein, Stil: Schlicht und Edel, ca 9,5 x 9,5 cm / Schwarz/weiß max. silber und Gold (Logo muss nicht unbedingt ersichtlich sein)
Bezeichnung: quiet harbor;
limited edion weingut brandt
Angefügt sind unsere bisherige Etikette weißwein: DAC.jpg u. Rotwein: roesler.jpg
bzw. in welche Richtung es gehen soll: Magnnum.pdf

```html
<!DOCTYPE html>
<html lang="de">
<head>
<meta charset="utf-8">
<title>Weingut Brandt – Quiet Harbor Etikett</title>
<link rel="stylesheet" href="https://fonts.googleapis.com/css2?family=Oswald:wght@300;400&display=swap">
<style>
  :root {
    --canvas: #ffffff;
    --label: #000000;
    --ink: #ffffff;
    --gold: #8a7438;
    --gold-soft: rgba(138, 116, 56, 0.35);
  }
  html, body {
    margin: 0;
    padding: 0;
    width: 1121px;
    height: 1200px;
    overflow: hidden;
    background: var(--canvas);
  }
  .canvas {
    position: relative;
    width: 1121px;
    height: 1200px;
  }
  .label {
    position: absolute;
    left: 110px;
    top: 150px;
    width: 900px;
    height: 900px;
    background: var(--label);
    color: var(--ink);
    font-family: "Oswald", sans-serif;
  }
  .ornament {
    position: absolute;
    width: 190px;
    height: 190px;
    background: radial-gradient(circle at center, var(--gold-soft) 0%, rgba(138,116,56,0.12) 55%, transparent 75%);
  }
  .ornament--tl { left: 70px;  top: 60px; }
  .ornament--tr { left: 635px; top: 65px; }
  .ornament--bl { left: 65px;  top: 625px; }
  .ornament--br { left: 635px; top: 625px; }

  .winery {
    position: absolute;
    left: 443px;
    top: 98px;
    margin: 0;
    font-weight: 400;
    font-size: 30px;
    line-height: 1;
  }
  .brand {
    position: absolute;
    left: 338px;
    top: 140px;
    margin: 0;
    font-weight: 300;
    font-size: 160px;
    line-height: 146px;
    letter-spacing: 0.08em;
  }
  .brand span { display: block; }
  .wine-name {
    position: absolute;
    left: 343px;
    top: 600px;
    margin: 0;
    font-weight: 300;
    font-size: 50px;
    line-height: 1;
  }
  .edition {
    position: absolute;
    left: 343px;
    top: 740px;
    margin: 0;
    font-weight: 300;
    font-size: 32px;
    line-height: 1;
  }
</style>
</head>
<body>
  <main class="canvas">
    <section class="label">
      <div class="ornament ornament--tl" role="img" aria-label="Goldenes Eckornament"></div>
      <div class="ornament ornament--tr" role="img" aria-label="Goldenes Eckornament"></div>
      <div class="ornament ornament--bl" role="img" aria-label="Goldenes Eckornament"></div>
      <div class="ornament ornament--br" role="img" aria-label="Goldenes Eckornament"></div>

      <p class="winery">weingut</p>
      <h1 class="brand"><span>BRA</span><span>NDT</span></h1>
      <p class="wine-name">quiet harbor</p>
      <p class="edition">LIMITED EDITION</p>
    </section>
  </main>
</body>
</html>
```